Chatterwall Timeline and profile images Design Project

Am looking to get 3-4 time line & 2-3 profile designs for my Chatterwall page, to keep my chtw page fun i want to have choices of images to change every now and then. This way i can keep my page fun and engaging with new designs. we are a Ecommerce website which is launching soon. we are based in the United Arab Emirates and our customers are based in Dubai and other cities in UAE, In addition to our neighbour countries in the GCC. We sell Gadgets, fashion and other trendy stuff that are hard to find in our market. The company name is "ZUBITRAKE" logo consists of a panda wearing traditional local Arab thobe. My website address will be www.zubitrake.com and Chatterwall page address is Chatterwall.com/zubitrakeuae . I will attach my logo and a screenshot of my website will look like to give you taste of the design. I want to keep the design simple and fun which will engage my customers and let the vist my page.
Updates

Hi,

i changed the required timeline designs from 4-6 to 3-4

i hope you find it fair.

Regards

Tarek

Industry/Entity Type

Fashion

Requirements
Nice to have
• buildings to relate to my country, maybe Manar Sidra, Qimmat al Sahil and the sable pillars. we have many nice buildings we can use from Dubai.
if you enter this website http://kirumelo.com/ and scroll to the bottom and see the beautiful buildings they have.

also a relation ship to shopping would be nice.

if you can apply the above to 2 out of the 4 designs for timeline i required .

Thanks

```html
<!DOCTYPE html>
<html lang="en">
<head>
<meta charset="utf-8">
<title>ZUBITRAKE – Chatterwall timeline covers</title>
<link rel="stylesheet" href="https://fonts.googleapis.com/css2?family=Comfortaa:wght@700&family=Carlito&display=swap">
<style>
  :root {
    --board-left: #5ec3e0;
    --board-right: #eef6fa;
    --panel: #ffffff;
    --panel-edge: #d9dde0;
    --brand-red: #a8191c;
    --cart-blue: #bfe6f5;
    --cart-ring: #ffffff;
    --caption: #ffffff;
    --frame: #e6e6e6;
  }
  * { box-sizing: border-box; margin: 0; padding: 0; }
  html, body { width: 1200px; height: 1000px; overflow: hidden; }
  body {
    position: relative;
    background: linear-gradient(100deg, var(--board-left) 0%, #a9dcec 45%, var(--board-right) 100%);
    font-family: "Carlito", "Calibri", sans-serif;
  }
  .cover {
    position: absolute;
    left: 125px;
    width: 963px;
    background: var(--panel);
  }
  .cover--bags { top: 66px; height: 421px; }
  .cover--city { top: 525px; height: 421px; }

  .bags-photo {
    position: absolute;
    left: 130px; top: 36px;
    width: 730px; height: 320px;
    background: linear-gradient(90deg, #7b3fe0 0%, #4a6cf0 22%, #f08a2e 40%, #2fb4ea 55%, #e8358f 75%, #ffc21a 100%);
    border-radius: 6px;
  }
  .city-photo {
    position: absolute;
    inset: 0 0 63px 0;
    background:
      linear-gradient(180deg, rgba(120,150,190,0.9) 0%, rgba(200,185,160,0.6) 35%, rgba(0,0,0,0) 55%),
      linear-gradient(90deg, #6b5a3a 0%, #b08a5c 30%, #8a9a8a 55%, #b8895a 80%, #7a6040 100%);
  }

  .brand-name {
    position: absolute;
    font-family: "Comfortaa", sans-serif;
    font-weight: 700;
    color: var(--brand-red);
    letter-spacing: 2px;
    line-height: 1;
  }
  .cover--bags .brand-name { left: 258px; top: 222px; font-size: 74px; }
  .cover--city .brand-name { left: 330px; top: 58px; font-size: 70px; }

  .profile-frame {
    position: absolute;
    left: 20px;
    width: 189px; height: 191px;
    border: 3px solid var(--frame);
    border-radius: 3px;
    box-shadow: 0 1px 3px rgba(0,0,0,0.25);
  }
  .cover--bags .profile-frame { top: 196px; background: rgba(255,255,255,0.92); }
  .cover--city .profile-frame { top: 195px; background: rgba(110,110,70,0.35); }

  .mascot {
    position: absolute;
    background: linear-gradient(180deg, #f2f2f2 0%, #dcdcdc 100%);
    border-radius: 40px 40px 12px 12px;
  }
  .cover--bags .mascot { left: 40px; top: 8px; width: 106px; height: 168px; }
  .cover--city .mascot { left: 55px; top: 38px; width: 112px; height: 158px; }

  .cart-badge {
    position: absolute;
    left: 22px; top: 26px;
    width: 116px; height: 116px;
    border-radius: 50%;
    background: radial-gradient(circle at 40% 35%, #e6f6fc 0%, var(--cart-blue) 70%);
    border: 3px solid var(--cart-ring);
    display: flex; align-items: center; justify-content: center;
  }
  .shop-arrow { position: absolute; left: 165px; top: 90px; }
  .shop-caption {
    position: absolute;
    left: 216px; top: 303px;
    font-size: 36px;
    color: var(--caption);
    text-shadow: 0 1px 3px rgba(0,0,0,0.35);
  }
</style>
</head>
<body>
  <section class="cover cover--bags">
    <div class="bags-photo" role="img" aria-label="Row of colourful glossy shopping bags with city skyline reflections"></div>
    <div class="brand-name">ZUBITRAKE</div>
    <div class="profile-frame">
      <div class="mascot" role="img" aria-label="Brand mascot panda in traditional Arab thobe and headdress"></div>
    </div>
  </section>

  <section class="cover cover--city">
    <div class="city-photo" role="img" aria-label="Blurred Dubai waterfront with palm trees, traditional buildings and a sail-shaped hotel tower"></div>
    <div class="brand-name">ZUBITRAKE</div>
    <div class="mascot" role="img" aria-label="Brand mascot panda in traditional Arab thobe and headdress"></div>
    <svg class="shop-arrow" width="130" height="200" viewBox="0 0 130 200" aria-hidden="true">
      <path d="M10 18 C 110 5, 135 120, 50 185" fill="none" stroke="#fff" stroke-width="4" stroke-linecap="round"/>
      <path d="M48 165 L50 186 L70 180" fill="none" stroke="#fff" stroke-width="4" stroke-linecap="round" stroke-linejoin="round"/>
    </svg>
    <div class="profile-frame">
      <div class="cart-badge">
        <svg width="80" height="70" viewBox="0 0 80 70" aria-label="Shopping cart" role="img">
          <path d="M4 8 H16 L24 44 H64 L72 16 H20" fill="none" stroke="#a8191c" stroke-width="7" stroke-linejoin="round" stroke-linecap="round"/>
          <circle cx="30" cy="58" r="6" fill="#a8191c"/>
          <circle cx="58" cy="58" r="6" fill="#a8191c"/>
        </svg>
      </div>
    </div>
    <p class="shop-caption">It’s time to shop</p>
  </section>
</body>
</html>
```